Beauty Clinic Treatment Menu (Lumen Nails & Beauty)

Needing a treatment menu designed for a beauty clinic in Whitianga, New Zealand. Like the colours grey, pink, white.
Elegant, Modern and feminine

Lumen Nails & Beauty
Karen Pell
Room3, 48 Tainui Street
Whitianga
0273816240
Karen.lumen@mailbox.test
lumenbeauty.co.nz

Target Market(s)

Females

Industry/Entity Type

Beauty Salon

Font styles to use
Serif

Colors

Requirements
Must have
• Chatterly and Snapgrid logo

```html
<!DOCTYPE html>
<html lang="en">
<head>
<meta charset="utf-8">
<title>Lumen Nails &amp; Beauty – Treatment Menu</title>
<link rel="stylesheet" href="https://fonts.googleapis.com/css2?family=Oswald:wght@200;300&display=swap">
<style>
  :root{
    --grey-band:#ababab;
    --pink:#e7c6dc;
    --peach:#f8cdb0;
    --dot-grey:#aaaaaa;
    --ink:#1e1e1e;
    --body:#555555;
    --brand:#5e4a55;
    --trim:#29abe2;
    --bleed:#ec008c;
    --paper:#ffffff;
  }
  html,body{margin:0;padding:0;overflow:hidden;background:var(--paper);}
  .menu{display:block;width:1200px;height:933px;font-family:"Oswald",sans-serif;font-weight:200;}
  .band-grey{fill:var(--grey-band);}
  .band-pink{fill:var(--pink);}
  .guide-trim{fill:none;stroke:var(--trim);stroke-width:.8;}
  .guide-fold{stroke:var(--trim);stroke-width:.8;}
  .guide-bleed{fill:none;stroke:var(--bleed);stroke-width:.8;stroke-dasharray:14 12;}
  .section-title{font-size:41px;fill:var(--ink);}
  .section-title.on-band{fill:var(--paper);}
  .sub-title{font-size:29px;fill:var(--ink);}
  .item{font-size:20px;fill:var(--body);}
  .facial-note{font-size:22px;fill:var(--body);}
  .duration{font-size:28px;fill:#333;}
  .price-line{font-size:23px;fill:var(--body);}
  .dot-pink{fill:var(--pink);}
  .dot-peach{fill:var(--peach);}
  .dot-grey{fill:var(--dot-grey);}
  .brand-name{font-size:25px;font-weight:200;fill:var(--brand);letter-spacing:1px;}
</style>
</head>
<body>
<svg class="menu" viewBox="0 0 1200 933" xmlns="http://www.w3.org/2000/svg">
  <path class="band-grey" d="M0 0H1200V71C1120 60 1050 50 990 55C900 62 840 80 800 114C730 60 660 38 560 38C440 38 360 115 187 115C110 115 40 100 0 88Z"/>
  <path class="band-pink" d="M0 747C60 712 140 700 220 700C420 700 520 840 700 868C860 892 940 764 1140 764C1170 764 1190 770 1200 780V933H0Z"/>

  <rect class="guide-trim" x="26" y="26" width="1146" height="879"/>
  <line class="guide-fold" x1="408" y1="0" x2="408" y2="933"/>
  <line class="guide-fold" x1="800" y1="0" x2="800" y2="933"/>
  <rect class="guide-bleed" x="14" y="12" width="1173" height="907"/>

  <g class="panel-nails">
    <text class="section-title on-band" x="76" y="88">NAILS</text>
    <circle class="dot-pink" cx="200" cy="71" r="25"/>

    <circle class="dot-pink" cx="98" cy="144" r="13"/>
    <text class="sub-title" x="119" y="156">MANICURE</text>
    <text class="item" x="60" y="186">Gel Polish $45</text>
    <text class="item" x="60" y="210">Regular Polish $40</text>

    <circle class="dot-pink" cx="98" cy="240" r="13"/>
    <text class="sub-title" x="119" y="252">PEDICURE</text>
    <text class="item" x="60" y="288">Gel Polish $45</text>
    <text class="item" x="60" y="313">Regular Polish $40</text>

    <circle class="dot-pink" cx="98" cy="349" r="13"/>
    <text class="sub-title" x="119" y="360">LUXURY PEDICURE</text>
    <text class="item" x="60" y="390">Includes: soak, exfoliation, heel rasping</text>
    <text class="item" x="60" y="415">and massage</text>
    <text class="item" x="60" y="445">Gel Polish $60</text>
    <text class="item" x="60" y="470">Regular Polish $55</text>

    <circle class="dot-pink" cx="98" cy="496" r="13"/>
    <text class="sub-title" x="119" y="510">GEL REMOVAL &amp; NAIL TIDY</text>
    <text class="sub-title" x="119" y="545">$25</text>

    <circle class="dot-pink" cx="98" cy="576" r="13"/>
    <text class="sub-title" x="119" y="587">ADD ON</text>
    <text class="item" x="60" y="618">Gel Removal $5</text>
    <text class="item" x="60" y="643">FortiBase $5 per layer</text>
    <text class="item" x="60" y="668">Builder gel $10</text>
    <text class="item" x="60" y="692">Nail Art/Glitter $ POA</text>

    <text class="brand-name" x="200" y="812" text-anchor="middle">Lumen Nails &amp; Beauty</text>
  </g>

  <g class="panel-facials">
    <text class="section-title" x="452" y="103">FACIALS</text>
    <circle class="dot-peach" cx="615" cy="86" r="25"/>

    <circle class="dot-peach" cx="464" cy="149" r="13"/>
    <text class="sub-title" x="490" y="159">Deep Cleansing Facial $75</text>
    <text class="duration" x="490" y="195">45 minutes</text>
    <text class="facial-note" x="490" y="221">Removes build up of dead skin cells,</text>
    <text class="facial-note" x="490" y="247">leaves the skin feeling soft and hydrated.</text>

    <circle class="dot-peach" cx="464" cy="301" r="13"/>
    <text class="sub-title" x="490" y="314">Therapeutic Facial $105</text>
    <text class="duration" x="490" y="351">60 minutes</text>
    <text class="facial-note" x="490" y="376">Tailored to suit your skins specific needs.</text>

    <circle class="dot-peach" cx="464" cy="432" r="13"/>
    <text class="sub-title" x="490" y="441">Rejuvenaiton Facial $120</text>
    <text class="duration" x="490" y="477">60 minutes</text>
    <text class="facial-note" x="490" y="502">Active yet gentle treatment that facilitates</text>
    <text class="facial-note" x="490" y="529">dermal rejuvenation.</text>

    <circle class="dot-peach" cx="464" cy="578" r="13"/>
    <text class="sub-title" x="490" y="588">35% Glycolic Facial $120</text>
    <text class="duration" x="490" y="624">60 minutes</text>
    <text class="facial-note" x="490" y="650">Hydrating, deep exfoliation treatment</text>
    <text class="facial-note" x="490" y="676">improving skin texture and appearance.</text>

    <circle class="dot-peach" cx="464" cy="724" r="13"/>
    <text class="sub-title" x="490" y="734">Dermaplaning $120</text>
    <text class="facial-note" x="490" y="761">Creates a smooth and radiant skin surface.</text>
    <text class="facial-note" x="490" y="787">Also removes soft facial hair.</text>
  </g>

  <g class="panel-waxing">
    <text class="section-title" x="832" y="132">EYES</text>
    <circle class="dot-grey" cx="944" cy="115" r="25"/>
    <g class="price-list">
      <circle class="dot-grey" cx="891" cy="169" r="8"/><text class="price-line" x="908" y="176">Silken Lash Lift $115</text>
      <circle class="dot-grey" cx="891" cy="195" r="8"/><text class="price-line" x="908" y="202">Eyebrow Shape $19</text>
      <circle class="dot-grey" cx="891" cy="222" r="8"/><text class="price-line" x="908" y="229">Eyebrow Tint $18</text>
      <circle class="dot-grey" cx="891" cy="249" r="8"/><text class="price-line" x="908" y="256">Eyelash Tint $25</text>
      <circle class="dot-grey" cx="891" cy="275" r="8"/><text class="price-line" x="908" y="282">Eye Trio $45</text>
    </g>

    <text class="section-title" x="832" y="340">FACE</text>
    <circle class="dot-grey" cx="944" cy="324" r="25"/>
    <g class="price-list">
      <circle class="dot-grey" cx="891" cy="371" r="8"/><text class="price-line" x="908" y="378">Lip $115</text>
      <circle class="dot-grey" cx="891" cy="398" r="8"/><text class="price-line" x="908" y="405">Chin $19</text>
    </g>

    <text class="section-title" x="832" y="478">BODY</text>
    <circle class="dot-grey" cx="944" cy="463" r="25"/>
    <g class="price-list">
      <circle class="dot-grey" cx="891" cy="515" r="8"/><text class="price-line" x="908" y="522">Under Arm $20</text>
      <circle class="dot-grey" cx="891" cy="542" r="8"/><text class="price-line" x="908" y="549">1/2 Leg $35</text>
      <circle class="dot-grey" cx="891" cy="568" r="8"/><text class="price-line" x="908" y="575">Full Leg $55</text>
      <circle class="dot-grey" cx="891" cy="595" r="8"/><text class="price-line" x="908" y="602">1/2 Arm $30</text>
      <circle class="dot-grey" cx="891" cy="621" r="8"/><text class="price-line" x="908" y="628">Full Arm $40</text>
      <circle class="dot-grey" cx="891" cy="648" r="8"/><text class="price-line" x="908" y="655">Bikini $28</text>
      <circle class="dot-grey" cx="891" cy="675" r="8"/><text class="price-line" x="908" y="682">Extended Bikini $38</text>
      <circle class="dot-grey" cx="891" cy="701" r="8"/><text class="price-line" x="908" y="708">Brazilian (1st Time) $65</text>
      <circle class="dot-grey" cx="891" cy="728" r="8"/><text class="price-line" x="908" y="735">Brazilian (4–6 Weeks) $50</text>
      <circle class="dot-grey" cx="891" cy="755" r="8"/><text class="price-line" x="908" y="762">Patches $5</text>
    </g>
  </g>
</svg>
</body>
</html>
```